Exciting Poster Project: 4 posters for Employee Benefit Program

We are an entrepreneurial healthcare IT company that is creating an internal campaign to launch our 2017 Culture and Professional Development goals for our internal staff.

We need 4 posters utilizing the 4 campaign logos (attached) that are tied together visually into a cohesive campaign.

A PPT is included that shows the other wall art that currently exists on the walls. The new posters will share a space with these pieces.

The posters may be mounted side by side, or stand alone on a wall- so the design should work both ways. Each poster should include its own icon and the tag line provided along with topics provided that fall under this category. The posters size can be dictated by your design, but the text should be legible from a minimum of 8 feet away.

At the bottom of each poster should include all 4 icons in order to tie the entire campaign together (perhaps they can be arranged together like a diamond shape with the primary one as the biggest diamond)

Our company website for our external branding is: www.pelmaroq.com
We have included our branding guidelines for our external brand, and ppts and graphics for our internal brand.

1) Poster 1:
a. Header: Better Today Than Yesterday
b. Sub-title: Personal and Professional Growth
c. Description: We are committed to helping you build on your strengths and passions and support you your career advancement goals. We have a variety of training and development programs available to help you reach your top potential!
Leadership Development Programs
1. Supervisor Training
2. Women’s Leadership
3. Leadership Meet-Ups
4. MBA Program
Staff Development
1. Continuing Education Fund
2. Book Club
3. Pelmaroq University
4. Mentorship
5. Learning Libraries
6. Department Wide Training Events

2) Poster 2:
a. Header: Perform at Highest Capacity
b. Sub-title: Be Your Best Self
c. Description: We are committed to providing programs that bring focus to your health and overall personal wellness to encourage a well balanced life
i. Healthy Living
1. Health and wellness seminars
2. Nutrition: Fruit Delivery
ii. Fitness:
1. Step Challenge
2. Virtual 5k
3. Recess
4. Golf Lessons
5. Ping Pong Club
iii. Creativity:
1. Painting
2. Photography Club
3. Virtual Trivia
iv. Mental Health:
1. Massage Therapy
2. EAP Education
v. Financial
1. 401(k)
2. Retirement education/financial planning seminars
3. Global Insurance Program education

3) Poster 3:
a. Header: Passionate Urgent and Driven to Success
b. Sub-Header: Innovation and Strategy
c. Description: We are committed to helping you connect the dots both in the industry and with our internal goals , mission, and vision.
i. Quarterly All-Hands
ii. Lumiverse
1. Internally: Departmental and Product Updates
2. Externally: Industry Knowledge
3. Culturally: Peer to Peer Community

4) Poster 4:
a. Header: Succeed as a Team
b. Sub-Header: Cultivating Collaboration
c. Description: We are committed to creating a culture of appreciation, teamwork, and supporting an open communication. All feedback and ideas are welcome here!
i. Team Building Events
1. Employee Focused
a. Summer Picnic
b. Employee Appreciation
c. Diwali
d. Holiday Party
e. Department Appreciation
2. Family Friendly
a. Halloween
b. Bring your Kids to Work Day
3. Awards
a. Peer to Peer: QuickNod Awards
b. Leadership: Crest of Merit
4. Surveys
a. New Hire
b. Employee Engagement
Updates

Target Market(s)

Internal Employees

Industry/Entity Type

Healthcare

Font styles to use
Sans Serif

Requirements
Must have
• Job Type: Posters
• Task Outline: Create Vector Art for 4 icons and 4 posters
• Fonts and Styles to Use: SourceSansPro
Nice to have
• There is an attachment with suggested concepts and styles that we like.
Should not have
• The poster should not be very wordy or hard to read in passing.

```html
<!DOCTYPE html>
<html lang="en">
<head>
<meta charset="utf-8">
<title>Succeed as a Team</title>
<link rel="stylesheet" href="https://fonts.googleapis.com/css2?family=Source+Sans+3:wght@400;600;700;800&display=swap">
<style>
  :root {
    --navy: #1c2647;
    --orange: #ef5a24;
    --blue: #2d6cb5;
    --teal: #1f9aa6;
    --purple: #6b3c96;
    --white: #ffffff;
  }
  * { margin: 0; padding: 0; box-sizing: border-box; }
  html, body { width: 863px; height: 1200px; overflow: hidden; background: var(--white); }
  body { font-family: "Source Sans 3", "Source Sans Pro", Arial, sans-serif; color: var(--navy); }
  .poster { position: relative; width: 863px; height: 1200px; background: var(--white); }

  .hero-band {
    position: absolute; left: 0; top: 0; width: 863px; height: 430px;
    background: var(--navy);
  }
  .team-illustration {
    position: absolute; left: 246px; top: 20px; width: 370px; height: 390px;
    border-radius: 50%;
    background: radial-gradient(circle at 50% 50%, rgba(255,255,255,0.22) 0%, rgba(45,108,181,0.55) 45%, rgba(239,90,36,0.35) 70%, rgba(28,38,71,0) 72%);
  }

  .headline {
    position: absolute; left: 0; top: 468px; width: 863px; text-align: center;
    font-size: 86px; font-weight: 700; line-height: 1; letter-spacing: -1px; color: var(--navy);
  }
  .subhead {
    position: absolute; left: 30px; top: 562px;
    font-size: 50px; font-weight: 700; line-height: 1; color: var(--orange);
  }
  .intro {
    position: absolute; left: 30px; top: 626px; width: 805px;
    font-size: 31px; line-height: 1.2; color: var(--navy); text-align: justify;
  }

  .program-list { position: absolute; top: 785px; font-size: 21px; line-height: 1.25; }
  .program-list.col-1 { left: 30px; }
  .program-list.col-2 { left: 298px; }
  .program-list.col-3 { left: 585px; }
  .category { color: var(--orange); font-weight: 600; }
  .group { color: var(--blue); font-weight: 700; }
  .group + .item, .item { color: var(--navy); }
  .spacer { height: 26px; }

  .campaign-icons {
    position: absolute; left: 22px; top: 995px; width: 170px; height: 185px;
  }

  .brand {
    position: absolute; right: 26px; bottom: 30px;
    display: flex; flex-direction: column; align-items: center; gap: 6px;
  }
  .brand-mark { width: 44px; height: 44px; background: var(--orange); }
  .brand-name { font-size: 20px; font-weight: 700; color: var(--orange); }
</style>
</head>
<body>
<main class="poster">
  <section class="hero-band">
    <div class="team-illustration" role="img" aria-label="Illustration of figures in blue, orange and white joining hands in a circle"></div>
  </section>

  <h1 class="headline">Succeed as a Team</h1>
  <h2 class="subhead">Cultivating Collaboration</h2>
  <p class="intro">We are committed to creating a culture of appreciation, teamwork, and supporting an open communication. All feedback and ideas are welcome here!</p>

  <div class="program-list col-1">
    <div class="category">i. Team Building Events</div>
    <div class="group">1. Employee Focused</div>
    <div class="item">a. Summer Picnic</div>
    <div class="item">b. Employee Appreciation</div>
    <div class="item">c. Diwali</div>
    <div class="item">d. Holiday Party</div>
    <div class="item">e. Department Appreciation</div>
  </div>

  <div class="program-list col-2">
    <div class="spacer"></div>
    <div class="group">2. Family Friendly</div>
    <div class="item">a. Halloween</div>
    <div class="item">b. Bring your Kids to Work Day</div>
    <div class="spacer"></div>
    <div class="group">3. Awards</div>
    <div class="item">a. Peer to Peer: QuickNod Awards</div>
    <div class="item">b. Leadership: Crest of Merit</div>
  </div>

  <div class="program-list col-3">
    <div class="spacer"></div>
    <div class="group">4. Surveys</div>
    <div class="item">a. New Hire</div>
    <div class="item">b. Employee Engagement</div>
  </div>

  <svg class="campaign-icons" viewBox="0 0 170 185" role="img" aria-label="Cluster of the four campaign icons arranged as diamonds">
    <rect x="62" y="5" width="52" height="52" transform="rotate(45 88 31)" fill="var(--orange)"/>
    <rect x="18" y="60" width="52" height="52" transform="rotate(45 44 86)" fill="var(--purple)"/>
    <rect x="104" y="60" width="52" height="52" transform="rotate(45 130 86)" fill="var(--blue)"/>
    <rect x="50" y="104" width="64" height="64" transform="rotate(45 82 136)" fill="var(--teal)"/>
  </svg>

  <div class="brand">
    <div class="brand-mark"></div>
    <div class="brand-name">Pelmaroq</div>
  </div>
</main>
</body>
</html>
```